My Journey - Document to be Laminated

I need a document that is professionally designed. Attached are the files that you are needed to produce this document. The main file to follow is called "My Journey - DOC". I would like you to take the concept and produce it professionally. I think it is important to know that this is something that will be laminated and used by door-to-door representatives. So I need it to be designed in Photoshop so that I can change the pictures as needed to fit other students. The students go to the doors and share literature to help people with their health and to grow spiritually. This document will be something they will share to help the people at the door understand who they are and some of their goals in life. If possible, I would like the concept(s) of the attached picture "theme" to be in the background of all the images - but I still don't want it to be busy, so if it is even something in vector background that is fine.

Not sure why the upload function is not working on brush harbor for this project. So to download the files, please see the following link: https://www.parcelnook.net/sh/qk/tbwelx83pazrqumvhnse/Pics-for-Document.zip?key=wjd61mrtp0acqe5vyx8nbh4kz&tk=7pgh2wme&dl=0

Requirements
Should not have
• anyone with jewelry, more on the minimalistic side

```html
<!DOCTYPE html>
<html lang="en">
<head>
<meta charset="utf-8">
<title>My Journey</title>
<link rel="stylesheet" href="https://fonts.googleapis.com/css2?family=Montserrat:ital,wght@0,700;0,900;1,700&family=Cinzel:wght@600&family=Source+Sans+3:wght@400;600&display=swap">
<style>
  :root {
    --navy: #143a72;
    --red: #b5172b;
    --ink: #4a4a4a;
    --dash: #7f95b2;
    --footer: #1a3a6a;
  }
  * { margin: 0; padding: 0; box-sizing: border-box; }
  html, body { width: 848px; height: 1200px; overflow: hidden; }
  body {
    position: relative;
    background: linear-gradient(180deg, #f6f7f9 0%, #eff1f4 45%, #ebebec 100%);
    font-family: "Source Sans 3", sans-serif;
  }
  .backdrop-scene {
    position: absolute; inset: 0;
    background:
      radial-gradient(ellipse 260px 300px at 150px 860px, rgba(248,224,160,0.85) 0%, rgba(240,214,165,0.55) 45%, rgba(240,230,220,0) 100%),
      radial-gradient(ellipse 160px 260px at 60px 620px, rgba(138,90,50,0.45) 0%, rgba(138,90,50,0.15) 55%, rgba(138,90,50,0) 100%),
      radial-gradient(ellipse 520px 260px at 260px 1080px, rgba(196,172,150,0.5) 0%, rgba(210,195,180,0.25) 55%, rgba(230,225,220,0) 100%),
      radial-gradient(ellipse 380px 300px at 100px 780px, rgba(236,214,180,0.45) 0%, rgba(236,214,180,0) 100%);
  }
  .title {
    position: absolute; top: 48px; left: 0; width: 100%;
    text-align: center;
    font-family: "Montserrat", sans-serif; font-weight: 900;
    font-size: 60px; letter-spacing: -2px; line-height: 1;
  }
  .title .my { color: var(--navy); }
  .title .journey { color: var(--red); }
  .title-rule { position: absolute; left: 246px; top: 118px; }
  .section-nav {
    position: absolute; top: 151px; left: 0; width: 100%;
    text-align: center;
    font-family: "Montserrat", sans-serif; font-style: italic; font-weight: 700;
    font-size: 13.5px; color: var(--navy); word-spacing: 1px;
  }
  .section-nav .sep { font-style: normal; margin: 0 12px; }
  .connectors { position: absolute; left: 0; top: 0; }
  .photo-card {
    position: absolute;
    background: #fff; padding: 4px; border-radius: 7px;
    box-shadow: 0 3px 8px rgba(0,0,0,0.22);
  }
  .photo-card .photo { width: 100%; height: 100%; border-radius: 4px; }
  .card-dream { left: 82px; top: 244px; width: 262px; height: 165px; transform: rotate(-5deg); }
  .card-dream .photo { background: linear-gradient(180deg, #9fb4cc 0%, #f0b06a 45%, #6a6a78 75%, #3b3d4a 100%); }
  .card-family { left: 521px; top: 259px; width: 262px; height: 165px; transform: rotate(5deg); }
  .card-family .photo { background: linear-gradient(160deg, #d9dde3 0%, #b9aaa0 40%, #3a3a3e 80%, #2a2a2e 100%); }
  .card-growing { left: 327px; top: 510px; width: 166px; height: 232px; transform: rotate(-2deg); }
  .card-growing .photo { background: linear-gradient(180deg, #c8c0bc 0%, #e6ddcf 45%, #e9b784 70%, #8c8a8c 100%); }
  .card-roots { left: 506px; top: 852px; width: 258px; height: 155px; transform: rotate(1deg); }
  .card-roots .photo { background: linear-gradient(135deg, #c9dce8 0%, #d8d6d0 40%, #cfe1ec 70%, #b7d3e3 100%); }
  .story { position: absolute; text-align: center; }
  .story h2 {
    font-family: "Cinzel", serif; font-weight: 600;
    font-size: 23px; color: var(--navy); letter-spacing: 0.5px; line-height: 1.1;
  }
  .story p { font-size: 11.3px; line-height: 1.28; color: var(--ink); margin-top: 8px; }
  .story-dream { left: 119px; top: 434px; width: 220px; transform: rotate(-5deg); }
  .story-family { left: 533px; top: 440px; width: 210px; transform: rotate(5deg); }
  .story-growing { left: 305px; top: 762px; width: 206px; transform: rotate(-2.5deg); }
  .story-roots { left: 530px; top: 1026px; width: 200px; }
  .brand {
    position: absolute; left: 60px; top: 962px; width: 260px; text-align: center;
  }
  .brand-mark { width: 38px; height: 38px; border-radius: 50%; background: var(--red); margin: 0 auto 10px; }
  .brand-name {
    font-family: "Montserrat", sans-serif; font-weight: 900;
    font-size: 19px; line-height: 1.1; color: var(--red);
  }
  .brand-tagline {
    margin-top: 12px;
    font-family: "Montserrat", sans-serif; font-style: italic; font-weight: 700;
    font-size: 15px; line-height: 1.4; color: var(--navy);
  }
  .footer-band {
    position: absolute; left: 0; top: 1149px; width: 100%; height: 51px;
    background: var(--footer);
    color: #fff; text-align: center;
    font-family: "Source Sans 3", sans-serif; font-weight: 600;
    font-size: 15px; letter-spacing: 2.4px; line-height: 51px;
  }
</style>
</head>
<body>
  <div class="backdrop-scene" role="img" aria-label="Warm sunrise scene with silhouettes of two climbers helping each other up a cliff above misty mountains"></div>

  <h1 class="title"><span class="my">MY</span> <span class="journey">JOURNEY</span></h1>
  <svg class="title-rule" width="356" height="12" viewBox="0 0 356 12">
    <path d="M0 9 Q178 -4 356 9 Q178 1 0 9 Z" fill="var(--navy)"/>
  </svg>

  <nav class="section-nav">
    My Roots<span class="sep">•</span>Growing Up<span class="sep">•</span>My Family<span class="sep">•</span>My Dream
  </nav>

  <svg class="connectors" width="848" height="1200" viewBox="0 0 848 1200" fill="none" stroke="var(--dash)" stroke-width="1.6" stroke-dasharray="6 5">
    <path d="M353 268 Q455 285 504 347"/>
    <path d="M494 385 Q405 420 385 497"/>
    <path d="M514 672 Q610 700 623 836"/>
  </svg>

  <div class="photo-card card-dream"><div class="photo" role="img" aria-label="Graduate in cap and gown on a rooftop overlooking a city skyline at sunset"></div></div>
  <div class="photo-card card-family"><div class="photo" role="img" aria-label="Family selfie of four people smiling together indoors"></div></div>
  <div class="photo-card card-growing"><div class="photo" role="img" aria-label="Childhood photo of three young sisters posing together"></div></div>
  <div class="photo-card card-roots"><div class="photo" role="img" aria-label="Map of Mexico with a red location pin marking Mexico City"></div></div>

  <section class="story story-dream">
    <h2>My Dream</h2>
    <p>I dream of a future full of possibilities--<br>a future where education, dedication,<br>and faith open doors to impact lives<br>and build a better tomorrow.</p>
  </section>

  <section class="story story-family">
    <h2>My Family</h2>
    <p>They are my strength, my inspiration,<br>and my constant support. Together,<br>we believe in each other and in what<br>the future holds.</p>
  </section>

  <section class="story story-growing">
    <h2>Growning Up</h2>
    <p>These are my sisters and me.<br>We grew up together, sharng dreams,<br>challenges, and endless support.</p>
  </section>

  <section class="story story-roots">
    <h2>My Roots</h2>
    <p>I was born and raised in Mexico.<br>My roots have shaped who i am --<br>full of strength, cutlture, and hope.</p>
  </section>

  <div class="brand">
    <div class="brand-mark"></div>
    <div class="brand-name">NORTHFIELD YOUTH<br>PATHWAY</div>
    <div class="brand-tagline">Empowering Youth<br>Since 1998</div>
  </div>

  <footer class="footer-band">REAL STORIES. STRONG VALUES. BRIGHTER TOMORROWS.</footer>
</body>
</html>
```